Business Card Design Project

I own a dental practice and would like to use a logo that was recently designed to make business cards.
I am looking for a clean card with the following information on the card.

Halvorsen Dental Center (Using the logo)
Martin L. Halvorsen, D.D.S.
7234 Pinewick Ave. Suite B
Colorado Springs, CO 80547
(719) 482-6130
halvorsendentalcenter@mailbox-example.net
www.halvorsendentalcenter.example

Also a list of items on the back:
Services include

Family Dentistry
Cosmetic
Whitening
Tooth Colored Fillings
Crowns/Bridges
Implants/Tooth Replacement
Dentures
Root Canals
Updates

Just an FYI, I added an email address and website address.

I also added my Pic.  Please give designs with and without the pic

Thanks

Target Market(s)

20-70 U.S. Female that handles the household budget.

Industry/Entity Type

Dental

Requirements
Must have
• The logo is key. The color scheme of the logo is also key. The back of the business card should have the list of Dental Services offered at the practice. The front should be clean and professional looking. No cartoons. I will also include a picture of myself. I think that the final card may or may not include this picture, so the card designs should come with and without the picture. USE THE BLUE LOGO ONLY!!!
Should not have
• NO teeth should be on the card.

```html
<!DOCTYPE html>
<html lang="en">
<head>
<meta charset="utf-8">
<title>Halvorsen Dental Center – Business Cards</title>
<link rel="stylesheet" href="https://fonts.googleapis.com/css2?family=Arimo:wght@400;700&display=swap">
<style>
  :root {
    --page-bg: #e4e2de;
    --teal: #2b5f79;
    --teal-light: #5f8ea3;
    --card-white: #f1f1f0;
    --ink: #4a4a4a;
    --ink-soft: #6a6a6a;
    --on-teal: #ffffff;
    --rule-on-teal: rgba(255,255,255,0.35);
  }
  * { box-sizing: border-box; margin: 0; padding: 0; }
  html, body {
    width: 1200px; height: 900px; overflow: hidden;
    background: var(--page-bg);
    font-family: "Arimo", Arial, sans-serif;
  }
  .sheet {
    position: relative; width: 1200px; height: 900px;
    display: flex; align-items: center; justify-content: center; gap: 60px;
  }
  .card {
    width: 520px; height: 297px; position: relative;
    box-shadow: 0 6px 18px rgba(0,0,0,0.18);
  }
  /* Back of card */
  .card--back {
    background: var(--teal); color: var(--on-teal);
    display: flex; flex-direction: column; align-items: center;
    padding-top: 70px;
  }
  .brand {
    display: flex; align-items: center; gap: 12px;
    font-size: 24px; font-weight: 400; letter-spacing: 0.5px;
  }
  .brand__dot {
    width: 16px; height: 16px; border-radius: 50%;
  }
  .card--back .brand { color: var(--on-teal); }
  .card--back .brand__dot { background: var(--on-teal); }
  .back__rule {
    width: 300px; height: 1px; background: var(--rule-on-teal);
    margin: 42px 0 18px;
  }
  .services {
    list-style: none; text-align: center;
    font-size: 14.5px; line-height: 1.45;
  }
  .services .sep { margin: 0 5px; font-size: 10px; vertical-align: 2px; }
  /* Front of card */
  .card--front {
    background: var(--card-white); color: var(--ink);
  }
  .card--front .brand {
    position: absolute; left: 34px; top: 205px;
    color: var(--teal-light); font-size: 20px;
  }
  .card--front .brand__dot { background: var(--teal-light); width: 14px; height: 14px; }
  .contact {
    position: absolute; left: 270px; top: 38px; width: 232px;
    font-size: 11.5px; line-height: 1.4; color: var(--ink-soft);
  }
  .contact__name { font-size: 15px; color: var(--ink); }
  .contact__rule {
    height: 1px; background: var(--teal-light); margin: 9px 0 10px;
  }
  .contact__row { display: flex; gap: 8px; }
  .contact__key { color: var(--teal-light); width: 8px; }
  .contact__address { margin-top: 12px; }
  .contact__web { margin-top: 12px; }
</style>
</head>
<body>
<main class="sheet">
  <section class="card card--back" aria-label="Back of business card">
    <div class="brand"><span class="brand__dot"></span><span>Halvorsen Dental Center</span></div>
    <div class="back__rule"></div>
    <ul class="services">
      <li>Family Dentistry <span class="sep">●</span> Cosmetic <span class="sep">●</span> Whitening</li>
      <li>Tooth Colored Fillings <span class="sep">●</span> Crowns/Bridges</li>
      <li>Implants/Tooth Replacement <span class="sep">●</span> Dentures <span class="sep">●</span> Root Canals</li>
    </ul>
  </section>

  <section class="card card--front" aria-label="Front of business card">
    <div class="contact">
      <p class="contact__name">Martin L. Halvorsen, D.D.S.</p>
      <div class="contact__rule"></div>
      <p class="contact__row"><span class="contact__key">T</span><span>(719) 482-6130</span></p>
      <p class="contact__row"><span class="contact__key">E</span><span>halvorsendentalcenter@mailbox-example.net</span></p>
      <p class="contact__address">7234 Pinewick Ave. Suite B<br>Colorado Springs, CO 80547</p>
      <p class="contact__web">www.halvorsendentalcenter.example</p>
    </div>
    <div class="brand"><span class="brand__dot"></span><span>Halvorsen Dental Center</span></div>
  </section>
</main>
</body>
</html>
```